Social Media Infographic for White Paper

Am working on a white paper on social media use by C-Suite Executives, and hope to include some infographics. I would like some help designing the first infographic.

The master bit of information is that "66% of C-Suite Executives use social media for professional purpose."

Within that 66%
-70% post original content on a daily/weekly basis
-13% of professional users are lurkers
-40% plan to use social media even more in the future

After initial design will need to two versions of the infographic, one listing the source at the bottom in small print (Source: 2017 Venmoor Partners Executive Social Media Study), the other one with no source information.

Infographic design should be complimentary with my website: www.venmoorpartners.example, but use of green should be very limited, if at all.

Target Market(s)

New media, C-Suite Executives, Executive Coaches

Industry/Entity Type

Management Consulting

Font styles to use
Sans Serif

Requirements
Must have
• Infographic with data displayed in a easy to understand format that tells the story of C-Suite Executives that participate in social media for professional purposes.
Nice to have
• Complements website design - www.venmoor.example.
Should not have
• Limit use of green from website logo, which can be overpowering. Some is ok, but not too much

```html
<!DOCTYPE html>
<html lang="en">
<head>
<meta charset="utf-8">
<title>C-Suite Executives on Social Media</title>
<link href="https://fonts.googleapis.com/css2?family=Oswald:wght@300&family=Nunito+Sans:ital,wght@0,400;0,800;1,400;1,800&display=swap" rel="stylesheet">
<style>
  :root {
    --panel: #232624;
    --green: #5f9b3e;
    --white: #ffffff;
    --track: #f2f2f2;
    --ring: #2e312f;
    --icon: #d4d4d4;
    --frame: #8a8a8a;
    --ink: #1f1f1f;
    --muted: #555555;
    --figure-light: #f4f4f4;
    --figure-mid: #c9c9c9;
  }
  * { margin: 0; padding: 0; box-sizing: border-box; }
  html, body { width: 1200px; height: 927px; overflow: hidden; background: var(--white); }
  .infographic { position: relative; width: 1200px; height: 927px; font-family: "Nunito Sans", sans-serif; }
  .panel { position: absolute; left: 0; top: 0; width: 1200px; height: 824px; background: var(--panel); overflow: hidden; }
  .figure { position: absolute; top: 60px; height: 764px; }
  .figure--left { left: 0; width: 230px; background: linear-gradient(90deg, var(--figure-light) 0%, var(--figure-mid) 55%, rgba(201,201,201,0) 100%);
    clip-path: polygon(0 0, 40% 6%, 45% 28%, 100% 30%, 60% 42%, 58% 60%, 52% 100%, 0 100%); }
  .figure--right { right: 0; width: 250px; background: linear-gradient(270deg, var(--figure-light) 0%, var(--figure-mid) 55%, rgba(201,201,201,0) 100%);
    clip-path: polygon(100% 0, 58% 3%, 55% 28%, 0 30%, 40% 44%, 42% 60%, 46% 100%, 100% 100%); }
  .frame-lines { position: absolute; inset: 0; }
  .headline { position: absolute; left: 0; width: 1200px; top: 48px; text-align: center; padding-left: 0;
    font-family: "Oswald", sans-serif; font-weight: 300; font-size: 178px; line-height: 1; color: var(--green); letter-spacing: -4px; }
  .lead { position: absolute; left: 323px; top: 226px; font-size: 35px; line-height: 44px; color: var(--white); letter-spacing: 0.3px; }
  .networks { position: absolute; left: 408px; top: 349px; display: flex; gap: 16.5px; list-style: none; }
  .networks li { width: 29px; height: 29px; border-radius: 6px; background: #e6e6e6; box-shadow: 2px 3px 4px rgba(0,0,0,.5); }
  .connectors { position: absolute; inset: 0; }
  .stat { position: absolute; top: 650px; color: var(--white); }
  .stat__value { font-family: "Oswald", sans-serif; font-weight: 300; font-size: 58px; line-height: 1; color: var(--green); letter-spacing: -2px; }
  .stat__text { font-size: 23px; line-height: 29px; margin-top: 11px; }
  .stat__text strong { font-weight: 800; font-style: italic; }
  .stat--original { left: 154px; } .stat--original .stat__value { margin-left: 72px; }
  .stat--lurkers { left: 505px; } .stat--lurkers .stat__value { margin-left: 49px; }
  .stat--future { left: 812px; } .stat--future .stat__value { margin-left: 90px; }
  .footer { position: absolute; left: 0; top: 824px; width: 1200px; height: 103px; }
  .source { position: absolute; left: 94px; top: 24px; font-style: italic; font-size: 22px; line-height: 29px; color: var(--ink); }
  .divider { position: absolute; top: 26px; width: 2px; height: 52px; background: #e2e2e2; }
  .brand { position: absolute; left: 527px; top: 20px; display: flex; align-items: center; gap: 10px; }
  .brand__mark { width: 58px; height: 58px; border-radius: 50%; background: var(--green); }
  .brand__name { font-weight: 800; font-size: 24px; line-height: 24px; color: var(--ink); }
  .site { position: absolute; left: 794px; top: 36px; font-size: 21px; letter-spacing: 1.3px; color: var(--muted); }
</style>
</head>
<body>
<main class="infographic">
  <section class="panel">
    <div class="figure figure--left" role="img" aria-label="Silhouette of an executive holding a tablet, surrounded by faint social network symbols"></div>
    <div class="figure figure--right" role="img" aria-label="Silhouette of an executive holding a tablet, surrounded by faint social network symbols"></div>

    <svg class="frame-lines" width="1200" height="824" viewBox="0 0 1200 824" aria-hidden="true">
      <path d="M250 0 L220 180 Q215 205 235 225 Q250 245 240 280 Q220 340 180 365 Q150 378 92 384" fill="none" stroke="var(--frame)" stroke-width="3"/>
      <path d="M950 0 L980 180 Q985 205 965 225 Q950 245 960 280 Q980 340 1020 365 Q1050 378 1108 388" fill="none" stroke="var(--frame)" stroke-width="3"/>
    </svg>

    <h1 class="headline">66%</h1>
    <p class="lead">of C-Suite Executives use social<br>media for professional purpose.</p>

    <ul class="networks" aria-label="Social networks">
      <li></li><li></li><li></li><li></li><li></li><li></li><li></li>
    </ul>

    <svg class="connectors" width="1200" height="824" viewBox="0 0 1200 824" aria-hidden="true">
      <path d="M258 485 Q265 420 335 420 L860 420 Q915 420 922 485" fill="none" stroke="#9a9a9a" stroke-width="4"/>
      <line x1="588" y1="420" x2="588" y2="478" stroke="#e8e8e8" stroke-width="5"/>
      <line x1="443" y1="528" x2="443" y2="736" stroke="#8a8a8a" stroke-width="2" stroke-dasharray="16 22"/>
      <line x1="749" y1="524" x2="749" y2="732" stroke="#8a8a8a" stroke-width="2" stroke-dasharray="16 22"/>

      <g class="ring ring--original" transform="translate(268 558)">
        <circle r="72" fill="var(--ring)"/>
        <circle r="57" fill="none" stroke="var(--white)" stroke-width="16"/>
        <circle r="57" fill="none" stroke="var(--green)" stroke-width="16" stroke-dasharray="250.7 358.1" transform="rotate(-90)"/>
        <circle r="47" fill="var(--track)"/>
        <g fill="none" stroke="var(--icon)" stroke-width="2.5">
          <path d="M-20 -28 H8 L18 -18 V28 H-20 Z"/>
          <path d="M-13 -14 H6 M-13 -6 H8 M-13 2 H2"/>
          <path d="M-10 18 Q-4 8 2 18 Q8 12 12 14"/>
          <path d="M26 -12 L6 14 L4 20 L10 17 L30 -8 Z"/>
        </g>
      </g>

      <g class="ring ring--lurkers" transform="translate(588 554)">
        <circle r="72" fill="var(--ring)"/>
        <circle r="57" fill="none" stroke="var(--white)" stroke-width="16"/>
        <circle r="57" fill="none" stroke="var(--green)" stroke-width="16" stroke-dasharray="46.6 358.1" transform="rotate(-90)"/>
        <circle r="47" fill="var(--track)"/>
        <path d="M-36 0 Q0 -34 36 0 Q0 34 -36 0 Z" fill="var(--icon)"/>
        <circle r="15" fill="var(--track)"/>
        <circle r="10" fill="var(--icon)"/>
      </g>

      <g class="ring ring--future" transform="translate(916 558)">
        <circle r="72" fill="var(--ring)"/>
        <circle r="57" fill="none" stroke="var(--white)" stroke-width="16"/>
        <circle r="57" fill="none" stroke="var(--green)" stroke-width="16" stroke-dasharray="143.2 358.1" transform="rotate(-90)"/>
        <circle r="47" fill="var(--track)"/>
        <g fill="var(--icon)">
          <rect x="-22" y="10" width="10" height="18"/>
          <rect x="-8" y="-2" width="10" height="30"/>
          <rect x="6" y="-14" width="10" height="42"/>
        </g>
        <path d="M-24 2 Q-8 -6 0 -26" fill="none" stroke="var(--icon)" stroke-width="3"/>
        <path d="M-6 -24 L2 -32 L6 -20 Z" fill="var(--icon)"/>
      </g>
    </svg>

    <div class="stat stat--original">
      <p class="stat__value">70%</p>
      <p class="stat__text">post <strong>original content</strong><br>on a daily/weekly basis</p>
    </div>
    <div class="stat stat--lurkers">
      <p class="stat__value">13%</p>
      <p class="stat__text">of professional<br>users are <strong>lurkers</strong></p>
    </div>
    <div class="stat stat--future">
      <p class="stat__value">40%</p>
      <p class="stat__text">plan to use social media<br>even more in the future</p>
    </div>
  </section>

  <footer class="footer">
    <p class="source">Source: 2017 Venmoor Partners<br>Executive Social Media Study</p>
    <span class="divider" style="left:476px"></span>
    <div class="brand">
      <span class="brand__mark"></span>
      <span class="brand__name">Venmoor<br>Partners</span>
    </div>
    <span class="divider" style="left:768px"></span>
    <p class="site">www.venmoorpartners.example</p>
  </footer>
</main>
</body>
</html>
```